Falcon Letterhead

Looking for a design template for our company’s official letterheads & business cards.It has to be mainly white and include our company logo, website, social media handle, address, phone number. Visit our website to have an idea of our brand identity and colours. Please use the same font that we are using in our website.
Target Market(s)
Lubricants & Greases, Industrial markets, Automotive
Font styles to use
Other font styles liked:
- Saira Extra-Condensed
Colors
ffffff
000000
fbee3f
Requirements
Must have
- It must be consistent with our brand identity. It must use the same exact yellow (Pantone color: 102C) and black (Pantone color: K100) as our brand colors.
- Must also use our font attached (Saira.zip). It's called Saira Extra-Condensed.
- We intend to use the FALCON logo and not the small mini-FN logo.
- On the design we must include ALL of the following:
- E-mail: info@falconoils.example
- @FalconGreases
- www.falconoils.example
- Address: P.O. Boc 4728, Qurain 53004, Kuwait
- Phone: (+965) 24718395
- Gulf Marwa Oils logo (attached). The logo attached is in Blue/Red but you can select one solid color for all of it such as BLACK or YELLOW depending on what background color you'll select.
Nice to have
- Like it to be as professional and as modern as possible. It has look clean, slick and classy.
Should not have
- Too many different colors.

```html
<!DOCTYPE html>
<html lang="en">
<head>
<meta charset="utf-8">
<title>Falcon Stationery</title>
<link href="https://fonts.googleapis.com/css2?family=Saira+Extra+Condensed:wght@400;600;700&family=Questrial&display=swap" rel="stylesheet">
<style>
  :root {
    --backdrop: #e3e3e3;
    --brand-black: #272526;
    --brand-yellow: #e6d812;
    --paper: #ffffff;
    --ink: #555555;
    --ink-soft: #8a8a8a;
    --signature-blue: #2b6cb8;
  }
  * { margin: 0; padding: 0; box-sizing: border-box; }
  html, body { width: 1200px; height: 966px; overflow: hidden; }
  body {
    position: relative;
    background: var(--backdrop);
    font-family: "Questrial", sans-serif;
  }
  .condensed { font-family: "Saira Extra Condensed", sans-serif; }

  /* Business card – back */
  .card-back {
    position: absolute; left: 226px; top: 473px; width: 234px; height: 410px;
    background: var(--brand-yellow);
    border-radius: 6px 14px 46px 46px;
    overflow: hidden;
  }
  .card-back .wordmark { position: absolute; left: 0; top: 12px; }
  .card-back .parent-mark {
    position: absolute; left: 72px; bottom: 38px;
    display: flex; align-items: center; gap: 6px;
  }

  /* Business card – front */
  .card-front {
    position: absolute; left: 78px; top: 238px; width: 233px; height: 412px;
    background: var(--brand-black);
    border-radius: 4px 4px 46px 4px;
    color: #ffffff;
  }
  .card-front .wordmark { position: absolute; left: 10px; top: 10px; }
  .holder { position: absolute; right: 22px; top: 132px; text-align: right; }
  .holder-name { color: var(--brand-yellow); font-weight: 700; font-size: 17px; line-height: 1; letter-spacing: .3px; }
  .holder-role { font-weight: 600; font-size: 10.5px; line-height: 1.3; }

  .contact-list { list-style: none; font-family: "Saira Extra Condensed", sans-serif; }
  .contact-list li { display: flex; align-items: flex-start; gap: 7px; }
  .contact-list svg { flex: none; margin-top: 2px; }
  .card-front .contact-list { position: absolute; left: 31px; top: 280px; font-size: 11.5px; line-height: 13.5px; color: #e6e6e6; }
  .card-front .contact-list li.address { margin-bottom: 7px; }

  /* Letterhead */
  .letterhead {
    position: absolute; left: 530px; top: 70px; width: 579px; height: 813px;
    background: var(--paper);
  }
  .letterhead-tab {
    position: absolute; right: 48px; top: 0; width: 140px; height: 133px;
    background: var(--brand-black);
    border-radius: 0 0 22px 22px;
    display: flex; align-items: center; justify-content: center;
  }
  .letter { position: absolute; left: 51px; top: 226px; width: 482px; color: var(--ink); }
  .salutation { font-size: 15px; color: #444; margin-bottom: 17px; }
  .letter-body p { font-size: 8.1px; line-height: 12.4px; text-align: justify; margin-bottom: 12px; }
  .closing { font-size: 8.1px; margin-top: 18px; }
  .signature {
    width: 104px; height: 44px; margin-top: 14px;
    background: linear-gradient(135deg, rgba(43,108,184,.18), rgba(43,108,184,.06));
    border-radius: 4px;
  }
  .letterhead .contact-list { position: absolute; left: 56px; top: 695px; font-size: 10px; line-height: 12px; color: #555; }
  .letterhead .contact-list li.address { margin-bottom: 4px; }
  .letterhead .parent-mark {
    position: absolute; right: 47px; top: 743px;
    display: flex; align-items: center; gap: 6px;
  }
  .parent-name { font-family: "Saira Extra Condensed", sans-serif; font-weight: 600; font-size: 10px; letter-spacing: .4px; }
  .parent-dot { width: 18px; height: 18px; border-radius: 50%; }
</style>
</head>
<body>

  <!-- Card back -->
  <section class="card-back">
    <svg class="wordmark" width="234" height="100" viewBox="0 0 234 100" aria-label="Falcon">
      <text x="4" y="86" textLength="214" lengthAdjust="spacingAndGlyphs"
            font-family="Saira Extra Condensed, sans-serif" font-weight="700" font-size="112" fill="#272526">FALCON</text>
    </svg>
    <div class="parent-mark">
      <span class="parent-dot" style="background:#272526"></span>
      <span class="parent-name" style="color:#272526">GULF MARWA OILS</span>
    </div>
  </section>

  <!-- Card front -->
  <section class="card-front condensed">
    <svg class="wordmark" width="214" height="100" viewBox="0 0 214 100" aria-label="Falcon">
      <text x="2" y="86" textLength="208" lengthAdjust="spacingAndGlyphs"
            font-family="Saira Extra Condensed, sans-serif" font-weight="700" font-size="112" fill="#e6d812">FALCON</text>
    </svg>
    <div class="holder">
      <div class="holder-name">JOHN SMITH</div>
      <div class="holder-role">CEO/FOUNDER</div>
    </div>
    <ul class="contact-list">
      <li class="address">
        <svg width="9" height="11" viewBox="0 0 10 12"><path d="M5 0a4 4 0 0 1 4 4c0 3-4 8-4 8S1 7 1 4a4 4 0 0 1 4-4z" fill="#e6d812"/><circle cx="5" cy="4" r="1.5" fill="#272526"/></svg>
        <span>P.O. Boc 4728<br>Qurain 53004, Kuwait</span>
      </li>
      <li><svg width="9" height="9" viewBox="0 0 10 10"><path d="M2 0l2 2-1 2c1 1 2 2 3 3l2-1 2 2-2 2C4 10 0 6 0 2z" fill="#e6d812"/></svg><span>(+965) 24718395</span></li>
      <li><svg width="9" height="8" viewBox="0 0 10 8"><rect width="10" height="8" fill="#e6d812"/><path d="M0 0l5 4 5-4" stroke="#272526" fill="none"/></svg><span>info@falconoils.example</span></li>
      <li><svg width="9" height="9" viewBox="0 0 10 10"><circle cx="5" cy="5" r="4.5" fill="#e6d812"/><path d="M1 5h8M5 .5v9" stroke="#272526" stroke-width=".8"/></svg><span>www.falconoils.example</span></li>
      <li><svg width="9" height="9" viewBox="0 0 10 10"><circle cx="5" cy="5" r="4" fill="#e6d812"/></svg><span>@FalconGreases</span></li>
    </ul>
  </section>

  <!-- Letterhead -->
  <section class="letterhead">
    <div class="letterhead-tab">
      <svg width="112" height="52" viewBox="0 0 112 52" aria-label="Falcon">
        <text x="2" y="45" textLength="108" lengthAdjust="spacingAndGlyphs"
              font-family="Saira Extra Condensed, sans-serif" font-weight="700" font-size="58" fill="#e6d812">FALCON</text>
      </svg>
    </div>

    <article class="letter">
      <p class="salutation">Dear Mr. Smith,</p>
      <div class="letter-body">
        <p>Lorem ipsum dolor sit amet, consectetur adipiscing elit. Donec orci purus, luctus vitae dignissim eu, iaculis sed purus. Vivamus faucibus, ipsum nec aliquet viverra, leo mauris condimentum ligula, sit amet sagittis enim ligula quis arcu. Nam egestas tortor id nisi porttitor mattis. In tortor ante, ultricies in suscipit a, tempus non massa. Vivamus et auctor mi. Fusce vel massa nulla. Phasellus nec eros mauris, et scelerisque orci.</p>
        <p>Donec malesuada orci vitae nulla accumsan porta a id massa. Quisque accumsan iaculis magna sit amet fringilla. Maecenas consequat, magna eget tincidunt semper, odio nibh rutrum mi, id feugiat ante nisi eu risus. Vestibulum nunc orci, rhoncus a placerat in, ultricies in mi. Cras mattis varius eros, vel fringilla nisi suscipit eget. Quisque scelerisque sagittis nulla at porttitor.</p>
        <p>Sed id augue vitae urna euismod commodo aliquet a quam. Pellentesque arcu velit, cursus et malesuada ut, consequat et diam. Nullam erat sem, rhoncus id ullamcorper vitae, rhoncus et arcu. In ultricies ultricies nulla, ut rutrum nisi iaculis at. Donec eu magna a metus ornare faucibus. Fusce aliquet faucibus ultricies. Morbi semper, est id tincidunt gravida, sem arcu adipiscing lacus, ac bibendum nulla leo eu purus. Quisque nec diam sed risus consectetur a cumsan quis nibh. Vestibulum id purus lorem.</p>
        <p>It is a long established fact that a reader will be distracted by the readable content of a page when looking at its layout. The point of using Lorem Ipsum is that it has a more-or-less normal distribution of letters, as opposed to using 'Content here, content here', making it look like readable English. Many desktop publishing packages</p>
      </div>
      <p class="closing">Sincerely,</p>
      <div class="signature" role="img" aria-label="Handwritten signature of John Smith in blue ink"></div>
    </article>

    <ul class="contact-list">
      <li class="address">
        <svg width="9" height="11" viewBox="0 0 10 12"><path d="M5 0a4 4 0 0 1 4 4c0 3-4 8-4 8S1 7 1 4a4 4 0 0 1 4-4z" fill="#e6d812"/><circle cx="5" cy="4" r="1.5" fill="#fff"/></svg>
        <span>P.O. Boc 4728,<br>Qurain 53004, Kuwait</span>
      </li>
      <li><svg width="9" height="9" viewBox="0 0 10 10"><path d="M2 0l2 2-1 2c1 1 2 2 3 3l2-1 2 2-2 2C4 10 0 6 0 2z" fill="#e6d812"/></svg><span>(+965) 24718395</span></li>
      <li><svg width="9" height="8" viewBox="0 0 10 8"><rect width="10" height="8" fill="#e6d812"/><path d="M0 0l5 4 5-4" stroke="#fff" fill="none"/></svg><span>info@falconoils.example</span></li>
      <li><svg width="9" height="9" viewBox="0 0 10 10"><circle cx="5" cy="5" r="4.5" fill="#e6d812"/><path d="M1 5h8M5 .5v9" stroke="#fff" stroke-width=".8"/></svg><span>www.falconoils.example</span></li>
      <li><svg width="9" height="9" viewBox="0 0 10 10"><circle cx="5" cy="5" r="4" fill="#e6d812"/></svg><span>@FalconGreases</span></li>
    </ul>

    <div class="parent-mark">
      <span class="parent-dot" style="background:#8a8a8a"></span>
      <span class="parent-name" style="color:#8a8a8a">GULF MARWA OILS</span>
    </div>
  </section>

</body>
</html>
```